Brightford Lingua Partners, LLC

We need a business card that includes information about our business and conveys a reliable business that provides document translation services and interpreters for a variety of corporate and individual clients. We want to come across as professional, reliable, yet approachable. It should include the following on one side:

ESL / ENL Language Classes, Private Lessons, and Online Tutors
PALQE Training and Testing
Translating & Interpreting Services
Contact us about Over-the-Phone Interpreting in over 200 languages
24/7/365
www.brightfordlingua.example

The other side should include (555) 481-3062

Marla Quennick, President
412 Garvin Ave., Ste. 209
Indianapolis, IN 46999
Updates

Please add USA as part of the address. Also, please add mrqquennick@brightfordlinguapartners.example as the e-mail address. Thank you.

Target Market(s)

Business professionals, their families, the international community

Industry/Entity Type

Business

Contact Information for Business Card

24/7/365
www.brightfordlingua.example

(555) 481-3062

Marla Quennick, President
412 Garvin Ave., Ste. 209
Indianapolis, IN 46999
USA

Font styles to use
Sans Serif

Colors

Designer to choose colors to be used in the design.

Requirements
Must have
• See project description
• e-mail address and web address
• Phone number
Nice to have
• a globe
• physical address
Should not have
• Should not have the same color scheme as other agencies in our market in Indiana unless it is blue and black. No purple or yellow.

```html
<!DOCTYPE html>
<html lang="en">
<head>
<meta charset="utf-8">
<title>Brightford Lingua Partners – Business Card</title>
<link href="https://fonts.googleapis.com/css2?family=Open+Sans:wght@400;600;700&display=swap" rel="stylesheet">
<style>
  :root{
    --brand-blue:#2a93d5;
    --brand-blue-dark:#1f7fbf;
    --tint:#edf6fc;
    --ink:#1f1f1f;
    --paper:#ffffff;
    --stage:#ffffff;
  }
  *{box-sizing:border-box;margin:0;padding:0}
  html,body{width:1200px;height:1200px;overflow:hidden;background:var(--stage)}
  body{font-family:"Open Sans",Arial,sans-serif;color:var(--ink);position:relative}
  .card{
    position:absolute;left:130px;width:940px;height:523px;
    background:var(--paper);border-radius:14px;overflow:hidden;
    box-shadow:0 10px 24px rgba(0,0,0,.22);
  }
  .card--back{top:52px}
  .card--front{top:625px}
  .band-top{position:absolute;left:0;top:0;width:100%;height:30px;background:var(--brand-blue)}
  .band-bottom{position:absolute;left:0;bottom:0;width:100%;height:82px;background:var(--brand-blue)}
  .band-rule{position:absolute;left:0;right:0;top:41px;height:3px;background:var(--paper)}

  /* back */
  .watermark{position:absolute;left:276px;top:37px;width:398px;height:398px;border-radius:50%;
    background:var(--tint)}
  .services{position:absolute;left:0;right:0;top:0;text-align:center;font-weight:600;font-size:23px}
  .services p{position:absolute;left:0;right:0;line-height:1;white-space:nowrap}
  .seal{position:absolute;left:448px;top:12px;width:60px;height:60px;border-radius:50%;
    background:var(--paper);border:4px solid var(--brand-blue);box-shadow:0 0 0 3px var(--paper)}
  .seal-gap{position:absolute;left:432px;top:30px;width:92px;height:22px;background:var(--brand-blue)}

  /* front */
  .brand{position:absolute;left:60px;top:87px;display:flex;align-items:center;gap:18px}
  .brand-dot{width:150px;height:150px;border-radius:50%;background:var(--brand-blue)}
  .brand-name{font-weight:600;font-size:40px;line-height:45px;color:var(--brand-blue-dark);white-space:nowrap}
  .brand-name small{font-size:17px}
  .name-tag{position:absolute;right:0;top:129px;width:250px;height:72px;background:var(--brand-blue);
    border-radius:8px 0 0 8px;color:var(--paper);padding:6px 22px 0 20px;text-align:right;white-space:nowrap}
  .name-tag .person{display:block;font-size:27px;line-height:33px;text-align:left}
  .name-tag .role{display:block;font-size:19px;line-height:24px}
  .contact{position:absolute;right:400px;font-size:18px;display:flex;align-items:center;gap:14px;white-space:nowrap}
  .contact svg{width:19px;height:19px;flex:none}
  .contact--phone{top:320px}
  .contact--mail{top:374px}
  .address{position:absolute;right:64px;top:318px;font-size:19px;line-height:30px;text-align:right;white-space:nowrap}
  .address-pin{position:absolute;right:38px;top:350px;width:19px;height:23px}
  .website{position:absolute;left:50%;top:25px;transform:translateX(-50%);
    background:var(--brand-blue);padding:0 12px;color:var(--paper);font-weight:700;font-size:31px;line-height:36px;white-space:nowrap}
</style>
</head>
<body>

<section class="card card--back" aria-label="Card back: services">
  <div class="band-top"></div>
  <div class="watermark" aria-hidden="true"></div>
  <div class="services">
    <p style="top:100px">ESL / ENL Language Classes, Private Lessons, and Online Tutors</p>
    <p style="top:158px">PALQE Training and Testing</p>
    <p style="top:227px">Translating &amp; Interpreting Services</p>
    <p style="top:288px">Contact us about Over-the-Phone</p>
    <p style="top:353px">Interpreting in over 200 languages</p>
    <p style="top:384px">24/7/365</p>
  </div>
  <div class="band-bottom">
    <div class="band-rule"></div>
    <div class="seal-gap"></div>
    <div class="seal" aria-hidden="true"></div>
  </div>
</section>

<section class="card card--front" aria-label="Card front: contact details">
  <div class="band-top"></div>

  <div class="brand">
    <div class="brand-dot" aria-hidden="true"></div>
    <div class="brand-name">Brightford<br>Lingua<br>Partners <small>LLC</small></div>
  </div>

  <div class="name-tag">
    <span class="person">Marla Quennick</span>
    <span class="role">President</span>
  </div>

  <div class="contact contact--phone">
    <span>(555) 481-3062</span>
    <svg viewBox="0 0 24 24" aria-hidden="true"><path fill="#2a93d5" d="M6.6 2.5l3 3.4-1.8 2.4c1.2 2.6 3.2 4.7 5.9 6l2.4-1.8 3.4 3-2.2 3.2C10 18 5.6 13.4 3.4 6.1z"/></svg>
  </div>
  <div class="contact contact--mail">
    <span>mrqquennick@brightfordlinguapartners.example</span>
    <svg viewBox="0 0 24 24" aria-hidden="true" fill="none" stroke="#2a93d5" stroke-width="1.6"><circle cx="12" cy="12" r="9.5"/><ellipse cx="12" cy="12" rx="4.2" ry="9.5"/><path d="M2.5 12h19M4 7h16M4 17h16"/></svg>
  </div>

  <div class="address">412 Garvin Ave., Ste. 209<br>Indianapolis, IN 46999<br>USA</div>
  <svg class="address-pin" viewBox="0 0 20 24" aria-hidden="true"><path fill="#2a93d5" d="M10 0C5 0 1.5 3.7 1.5 8.3 1.5 14 10 24 10 24s8.5-10 8.5-15.7C18.5 3.7 15 0 10 0zm0 11.5a3.3 3.3 0 110-6.6 3.3 3.3 0 010 6.6z"/></svg>

  <div class="band-bottom">
    <div class="band-rule"></div>
    <div class="website">www.brightfordlingua.example</div>
  </div>
</section>

</body>
</html>
```